Innovative Healthcare Technology Company needs a Business Card Design

We are in need of an innovative business card design for a new healthcare software company called "Brightwell Harbor Systems". We develop software that creates medical assessment applications and mobile e-learning prevention services to reduce risk behaviors in adolescent and young adults. Our initial product, the "MERIDIAN App", conducts a tailored sexual risk assessment and provides a doctor with an insightful patient report to improve sexual risk counseling and ultimately reduce unintended pregnancy, STDs, etc.

We would like the design to incorporate our logo and branding colors (attached) in an innovative and creative manner. The final design should communicate professionalism and healthcare innovation. Our tag line is "FORESIGHT IS THE BEST CARE" (doesn't necessarily need to be included) and our target audience is doctors, medical directors, and medical business administrators. Please visit our website for additional info ourlantrixhub.com. Be creative and we look forward to seeing your designs!

Target Market(s)

healthcare - doctors, medical directors and medical business administrators

Industry/Entity Type

Healthcare

Contact Information for Business Card

We would like the design to incorporate our logo and branding colors (attached) in an innovative and creative manner. The final design should communicate professionalism and healthcare innovation. Our tag line is "FORESIGHT IS THE BEST CARE" (doesn't necessarily need to be included)

Font styles to use
Other font styles liked:
• quicksand

Requirements
Must have
• our logo and brand colors
• Name, (Joan Ferraventi, PhD)
• Email (drjoan@ourlantrixhub.com)
• phone (555.213.8870)
• Website (ourlantrixhub.com)
Should not have
• cartoon look

```html
<!DOCTYPE html>
<html lang="en">
<head>
<meta charset="utf-8">
<title>Brightwell Harbor Systems – Business Card</title>
<link rel="stylesheet" href="https://fonts.googleapis.com/css2?family=Quicksand:wght@400;500;700&display=swap">
<style>
  :root {
    --backdrop: #3b3b3d;
    --brand-blue: #3c6192;
    --brand-blue-light: #5a86bd;
    --brand-green: #7d9e80;
    --brand-grey: #8a8a8a;
    --ink: #2b2b2b;
    --paper: #ffffff;
    --tint-blue: #c4cfdf;
    --tint-green: #dfe7e0;
    --tint-grey: #e3e3e3;
  }
  * { box-sizing: border-box; margin: 0; padding: 0; }
  html, body {
    width: 1200px; height: 900px; overflow: hidden;
    background: var(--backdrop);
    font-family: "Quicksand", sans-serif;
  }
  .canvas { position: relative; width: 1200px; height: 900px; }

  .card {
    position: absolute; width: 640px; height: 366px;
    overflow: hidden; box-shadow: 0 14px 30px rgba(0,0,0,.45);
  }

  /* Back side */
  .card-back { left: 70px; top: 70px; background: var(--brand-blue); }
  .card-back .pattern-area {
    position: absolute; right: 0; top: 0; width: 470px; height: 200px;
    background: radial-gradient(ellipse at 75% 30%, rgba(120,170,235,.45), rgba(60,97,146,0) 70%);
  }
  .card-back .edge-tint {
    position: absolute; left: 0; width: 80px; height: 72px;
    background: var(--brand-blue-light); opacity: .6;
    border-radius: 0 18px 18px 0;
  }
  .card-back .edge-tint-top { top: 112px; }
  .card-back .edge-tint-middle { top: 200px; }
  .card-back .edge-tint-bottom { top: 288px; height: 78px; }
  .card-back .wordmark {
    position: absolute; left: 150px; top: 212px;
    display: flex; align-items: center; gap: 12px;
  }
  .card-back .wordmark .mark-square {
    width: 22px; height: 22px; background: var(--paper); border-radius: 3px;
  }
  .card-back .wordmark .name {
    font-size: 30px; font-weight: 700; color: var(--paper); letter-spacing: .5px;
  }
  .card-back .tagline {
    position: absolute; left: 150px; top: 266px;
    font-size: 16px; letter-spacing: 1.5px; color: var(--paper); font-weight: 500;
  }

  /* Front side */
  .card-front { left: 490px; top: 460px; background: var(--paper); }
  .card-front .wordmark {
    position: absolute; left: 40px; top: 40px;
    display: flex; align-items: center; gap: 12px;
  }
  .card-front .wordmark .mark-square {
    width: 22px; height: 22px; background: var(--brand-blue); border-radius: 3px;
  }
  .card-front .wordmark .name {
    font-size: 28px; font-weight: 700; color: var(--brand-blue); letter-spacing: .5px;
  }
  .card-front .person {
    position: absolute; left: 40px; top: 112px;
    font-size: 20px; font-weight: 700; color: var(--brand-blue); letter-spacing: 1px;
  }
  .card-front .contact-list {
    position: absolute; left: 40px; top: 156px; list-style: none;
  }
  .card-front .contact-list li {
    display: flex; align-items: center; gap: 12px;
    font-size: 21px; color: var(--ink); letter-spacing: 1px; line-height: 34px;
  }
  .card-front .contact-list svg { width: 20px; height: 20px; flex: none; }
  .card-front .tint-block {
    position: absolute; width: 200px; height: 70px; border-radius: 16px;
  }
  .card-front .tint-grey { right: -30px; top: 40px; width: 90px; background: var(--tint-grey); }
  .card-front .tint-green { right: -30px; top: 124px; background: var(--tint-green); }
  .card-front .tint-blue { right: -30px; top: 224px; width: 300px; height: 160px; background: var(--tint-blue); }
  .card-front .footer-band {
    position: absolute; left: 0; bottom: 0; width: 360px; height: 44px;
    background: var(--brand-blue);
    display: flex; align-items: center; justify-content: center;
  }
  .card-front .footer-band span {
    color: var(--paper); font-size: 17px; font-weight: 500; letter-spacing: 1.5px;
  }
</style>
</head>
<body>
<main class="canvas">

  <section class="card card-back">
    <div class="pattern-area" role="img" aria-label="Network of linked hexagon outlines in light blue"></div>
    <div class="edge-tint edge-tint-top"></div>
    <div class="edge-tint edge-tint-middle"></div>
    <div class="edge-tint edge-tint-bottom"></div>
    <div class="wordmark">
      <span class="mark-square"></span>
      <span class="name">Brightwell Harbor Systems</span>
    </div>
    <p class="tagline">FORESIGHT IS THE BEST CARE</p>
  </section>

  <section class="card card-front">
    <div class="wordmark">
      <span class="mark-square"></span>
      <span class="name">Brightwell Harbor Systems</span>
    </div>
    <p class="person">Joan Ferraventi, PhD</p>
    <ul class="contact-list">
      <li>
        <svg viewBox="0 0 20 20" aria-hidden="true"><rect x="2" y="5" width="16" height="11" fill="#7d9e80"/><path d="M2 5 L10 11 L18 5" fill="none" stroke="#fff" stroke-width="1.5"/></svg>
        drjoan@ourlantrixhub.com
      </li>
      <li>
        <svg viewBox="0 0 20 20" aria-hidden="true"><path d="M5 3 C3 5 3 9 7 13 C11 17 15 17 17 15 L14 12 L12 13 C10 12 8 10 7 8 L8 6 Z" fill="#7d9e80"/></svg>
        555.213.8870
      </li>
      <li>
        <svg viewBox="0 0 20 20" aria-hidden="true"><circle cx="10" cy="10" r="8" fill="#7d9e80"/><g fill="none" stroke="#fff" stroke-width="1"><ellipse cx="10" cy="10" rx="3.5" ry="8"/><line x1="2" y1="10" x2="18" y2="10"/><line x1="3.5" y1="6" x2="16.5" y2="6"/><line x1="3.5" y1="14" x2="16.5" y2="14"/></g></svg>
        ourlantrixhub.com
      </li>
    </ul>
    <div class="tint-block tint-grey"></div>
    <div class="tint-block tint-green"></div>
    <div class="tint-block tint-blue"></div>
    <div class="footer-band"><span>FORESIGHT IS THE BEST CARE</span></div>
  </section>

</main>
</body>
</html>
```